Technology Company Web Design Project

We are working with BrimLoop. They are a technology company and in need of a new website design.
BrimLoop helps companies control who (or what) can access which information inside their systems — and under what conditions. Think of them as the traffic controller for digital access and data permissions.
Instead of letting every app, employee, or AI bot freely connect to everything, GateMarrow makes sure:
• Each one only gets access to what it actually needs.
• That access follows company rules automatically.
• Those rules are enforced the same way everywhere — across apps, servers, and even AI tools.
Some competitor sites to use for inspiration:
https://www.korvanshield.com/en/lp/ac/korvanmesh.html
https://www.dunmerecharter.org
https://www.qelvo.com
Thank you for taking the time to consider designing a website for us. We are web developers based in Stockton and Los Angeles, CA, USA. Most of our projects go through the same process. Understanding this process may help you win a project with us. We custom-code all of our websites in-house. We don’t have any requirements as to what tools you use for your design, but we prefer Figma files. For any design that we label as four-stars, we send it to the client for review. The client picks the final design they want us to use. Once we complete this process, we will continue to show additional clients all the four-star sites and purchase them later. Your designs will have multiple chances to sell. For better chances of success, we ask that you follow these guidelines.
IMAGES:
If you use any images or icons in the design, we ask that you have a link to the asset so we can purchase the image/icon. Most of the designs we submit do not have the customer’s images on them unless they have some great images. Be creative; show us the feeling you are trying to portray with your image choices. Use any royalty-free site you choose. We subscribe to Tarsel and mainly use their images, but we can purchase images outside of Tarsel.
PLEASE NOTE: we will not submit designs to clients with watermarks on the images.
FONTS:
We ask that you identify the fonts used in the design. This can be done in a message if you want. We typically use Google Fonts and Tarsel Fonts.
CONTENT:
We're always open to different content and ideas. We often submit designs with stock images so the client can see our vision. We typically take pictures after the website launch to use their images with our vision. Lorem Ipsum is fine for paragraphs, but we ask that you write the headers in correct English. We want to be able to show the vision and identify the sections of the website.
INSPIRATION:
We typically add a couple of links in the brief of websites we like to help you get started in your design.
REVISIONS:
We do not often ask for revisions of the designs unless we see something in the design that may not appeal to the client. If there are slight changes that we want to make, we do that in the development process.
FEEDBACK:
We rarely give feedback on designs during the design process. We are working on many website projects and do not have the time to provide feedback. We usually respond if your request is well thought out and asks specific questions, but a note asking “feedback, please” usually goes unanswered.

```html
<!DOCTYPE html>
<html lang="en">
<head>
<meta charset="utf-8">
<title>BrimLoop — Digital Access Control Platform</title>
<link href="https://fonts.googleapis.com/css2?family=Outfit:wght@500;600;700&family=Figtree:wght@400;500;600;700&display=swap" rel="stylesheet">
<style>
:root{
  --blue:#2563eb;
  --blue-dark:#1d4ed8;
  --ink:#0f172a;
  --text:#334155;
  --muted:#475569;
  --line:#dbe3f0;
  --badge:#dbe7fd;
  --hero-a:#e6e8f8;
  --hero-b:#dfe3f9;
  --tech-bg:#edf2fd;
  --footer:#141b2d;
  --footer-text:#aab3c5;
  --green:#22c55e;
  --white:#ffffff;
}
*{box-sizing:border-box;margin:0;padding:0}
html,body{width:1200px;height:2883px;overflow:hidden}
body{font-family:"Figtree",sans-serif;color:var(--ink);background:var(--white)}
h1,h2,h3,h4,.brand{font-family:"Outfit",sans-serif}
a{color:inherit;text-decoration:none}

.nav{height:67px;display:flex;align-items:center;justify-content:space-between;padding:0 35px 0 37px;background:var(--white);box-shadow:0 1px 0 #eef1f6}
.brand{display:flex;align-items:center;gap:10px;font-size:25px;font-weight:600;color:var(--ink)}
.brand-dot{width:14px;height:14px;border-radius:50%;background:var(--blue);flex:none}
.nav-links{display:flex;align-items:center;gap:34px;font-size:16px;color:var(--muted)}
.btn{display:inline-flex;align-items:center;justify-content:center;gap:10px;border-radius:6px;font-size:15px;font-weight:600;height:44px;padding:0 18px}
.btn-primary{background:var(--blue);color:var(--white)}
.nav .btn{height:42px;font-size:15px}

.hero{height:670px;background:linear-gradient(135deg,var(--hero-a),var(--hero-b));position:relative;padding:86px 0 0 34px}
.badge{display:inline-block;background:var(--badge);color:var(--blue-dark);font-size:12.5px;font-weight:500;padding:5px 12px;border-radius:999px}
.hero .badge{background:#e9ecfa}
.hero h1{font-size:63px;line-height:63px;font-weight:700;margin-top:22px;letter-spacing:-0.5px}
.hero h1 span{color:var(--blue)}
.hero-copy{font-size:20.5px;line-height:34.5px;color:var(--muted);width:545px;margin-top:18px}
.hero-actions{display:flex;gap:17px;margin-top:32px}
.hero-actions .btn{height:47px}
.btn-get{width:176px}
.btn-ghost{width:156px;border:1px solid #cfd8f5;color:var(--blue);background:transparent;font-weight:500}
.ticks{display:flex;gap:25px;margin-top:31px;font-size:14.5px;color:var(--muted)}
.ticks li{list-style:none;display:flex;align-items:center;gap:9px}
.hero-visual{position:absolute;left:625px;top:179px;width:539px;height:307px}
.hero-visual .back{position:absolute;inset:-10px -8px -14px -6px;background:#c9cdf3;border-radius:16px;transform:rotate(2deg)}
.hero-visual .art{position:absolute;inset:0;border-radius:14px;background:radial-gradient(ellipse at 50% 45%,#0e4a70 0%,#08223e 45%,#040b1f 100%);box-shadow:0 20px 40px rgba(30,40,90,.25)}

.features{height:808px;padding-top:48px;text-align:center}
.features h2{font-size:38px;font-weight:700;margin-top:18px}
.features .lead{font-size:20.5px;line-height:29px;color:var(--muted);width:820px;margin:14px auto 0}
.grid{display:grid;grid-template-columns:repeat(3,354px);column-gap:35px;row-gap:35px;margin:46px 0 0 35px;text-align:left}
.card{border:1px solid var(--line);border-radius:8px;padding:26px 26px 0 26px;background:var(--white)}
.card.tall{height:259px}
.card.short{height:238px}
.icon-box{width:51px;height:51px;border-radius:6px;background:var(--badge);display:flex;align-items:center;justify-content:center;color:var(--blue)}
.card h3{font-family:"Figtree",sans-serif;font-size:20px;font-weight:500;margin-top:30px;white-space:nowrap;letter-spacing:-0.2px}
.card p{font-size:14.5px;line-height:21px;color:var(--muted);margin-top:24px;width:285px}

.tech{height:669px;background:var(--tech-bg);position:relative;padding:51px 0 0 35px}
.tech h2{font-size:39px;line-height:43px;font-weight:700;margin-top:20px;width:540px}
.tech .lead{font-size:19px;line-height:30px;color:var(--muted);width:540px;margin-top:18px}
.points{list-style:none;margin-top:30px}
.points li{display:flex;gap:18px;margin-bottom:26px}
.points .dot{width:32px;height:32px;border-radius:50%;background:#dde6fb;display:flex;align-items:center;justify-content:center;flex:none;margin-top:4px}
.points h4{font-family:"Figtree",sans-serif;font-size:17px;font-weight:600}
.points p{font-size:16.5px;line-height:25px;color:var(--muted);margin-top:7px;width:470px}
.tech-visual{position:absolute;left:627px;top:211px;width:538px;height:240px;border-radius:14px;background:linear-gradient(120deg,#061329 0%,#0a3a7a 35%,#082451 55%,#1554b8 75%,#061329 100%);box-shadow:0 18px 36px rgba(20,30,70,.22)}

.cta{height:353px;background:var(--blue);text-align:center;color:var(--white);padding-top:52px}
.cta h2{font-size:40px;font-weight:700}
.cta p{font-size:20.5px;line-height:30px;color:#dbe5ff;width:640px;margin:24px auto 0}
.cta-actions{display:flex;justify-content:center;gap:17px;margin-top:34px}
.cta-actions .btn{height:46px}
.btn-white{background:var(--white);color:var(--blue);width:173px;font-weight:500}
.btn-outline{border:1.5px solid var(--white);color:var(--white);width:166px}

.footer{height:316px;background:var(--footer);padding:52px 35px 0;color:var(--footer-text)}
.footer-cols{display:grid;grid-template-columns:291px 291px 291px 257px}
.footer .brand{color:var(--white);font-size:22px;gap:8px}
.footer .brand-dot{background:#3b82f6;width:12px;height:12px}
.footer .tag{font-size:16px;line-height:26px;margin-top:14px;width:240px}
.footer h4{font-family:"Figtree",sans-serif;color:var(--white);font-size:16.5px;font-weight:600;margin-top:6px}
.footer ul{list-style:none;margin-top:18px;font-size:16px}
.footer li{margin-bottom:14px}
.footer-bottom{border-top:1px solid #262f44;margin-top:36px;padding-top:38px;text-align:center;font-size:16px}
</style>
</head>
<body>

<header class="nav">
  <a class="brand" href="#"><span class="brand-dot"></span>BrimLoop</a>
  <nav class="nav-links">
    <a href="#">Features</a>
    <a href="#">Benefits</a>
    <a href="#">Contact</a>
    <a class="btn btn-primary" href="#">Request Demo</a>
  </nav>
</header>

<section class="hero">
  <span class="badge">Digital Access Control Platform</span>
  <h1>Control Digital<br>Access Like a<br><span>Traffic Controller</span></h1>
  <p class="hero-copy">BrimLoop helps companies control who (or what) can access which information inside their systems — and under what conditions. Ensure each app, employee, or AI bot only gets access to what it actually needs.</p>
  <div class="hero-actions">
    <a class="btn btn-primary btn-get" href="#">Get Started
      <svg width="16" height="16" viewBox="0 0 24 24" fill="none" stroke="#fff" stroke-width="2.4" stroke-linecap="round"><path d="M5 12h14M13 6l6 6-6 6"/></svg>
    </a>
    <a class="btn btn-ghost" href="#">Watch Demo</a>
  </div>
  <ul class="ticks">
    <li><svg width="20" height="20" viewBox="0 0 24 24" fill="none" stroke="#22c55e" stroke-width="2"><circle cx="12" cy="12" r="9.5"/><path d="M8 12l3 3 5-6" stroke-linecap="round"/></svg>Enterprise Ready</li>
    <li><svg width="20" height="20" viewBox="0 0 24 24" fill="none" stroke="#22c55e" stroke-width="2"><circle cx="12" cy="12" r="9.5"/><path d="M8 12l3 3 5-6" stroke-linecap="round"/></svg>AI-Compatible</li>
    <li><svg width="20" height="20" viewBox="0 0 24 24" fill="none" stroke="#22c55e" stroke-width="2"><circle cx="12" cy="12" r="9.5"/><path d="M8 12l3 3 5-6" stroke-linecap="round"/></svg>Cross-Platform</li>
  </ul>
  <div class="hero-visual">
    <div class="back"></div>
    <div class="art" role="img" aria-label="Illustration of a locked phone connected to glowing security icons on a dark blue background"></div>
  </div>
</section>

<section class="features">
  <span class="badge">Core Features</span>
  <h2>Comprehensive Access Control Management</h2>
  <p class="lead">Enforce company rules automatically across apps, servers, and AI tools with our unified platform</p>
  <div class="grid">
    <article class="card tall">
      <div class="icon-box"><svg width="22" height="22" viewBox="0 0 24 24" fill="none" stroke="currentColor" stroke-width="2"><rect x="4" y="11" width="16" height="10" rx="2"/><path d="M8 11V7a4 4 0 018 0v4"/></svg></div>
      <h3>Access Control Management</h3>
      <p>Granular control over who can access what information, with dynamic permission management that adapts to your business needs.</p>
    </article>
    <article class="card tall">
      <div class="icon-box"><svg width="22" height="22" viewBox="0 0 24 24" fill="none" stroke="currentColor" stroke-width="2" stroke-linejoin="round"><path d="M12 3l7 3v5c0 4.5-3 8-7 10-4-2-7-5.5-7-10V6z"/></svg></div>
      <h3>Data Permissions Across Systems</h3>
      <p>Unified permission management across all your applications, databases, and services with consistent policy enforcement.</p>
    </article>
    <article class="card tall">
      <div class="icon-box"><svg width="22" height="22" viewBox="0 0 24 24" fill="none" stroke="currentColor" stroke-width="2" stroke-linejoin="round"><path d="M13 2L4 14h7l-1 8 9-12h-7z"/></svg></div>
      <h3>AI-Specific Access Controls</h3>
      <p>Advanced controls for AI systems and bots, ensuring they only access the data they need for their specific functions.</p>
    </article>
    <article class="card short">
      <div class="icon-box"><svg width="22" height="22" viewBox="0 0 24 24" fill="none" stroke="currentColor" stroke-width="2" stroke-linecap="round"><circle cx="9" cy="8" r="3.5"/><path d="M3 20c0-3.5 2.7-6 6-6s6 2.5 6 6M16 4.5a3.5 3.5 0 010 7M18 14c2 .8 3 3 3 6"/></svg></div>
      <h3>Role-Based Permissions</h3>
      <p>Flexible role management system that scales with your organization and adapts to changing team structures.</p>
    </article>
    <article class="card short">
      <div class="icon-box"><svg width="22" height="22" viewBox="0 0 24 24" fill="none" stroke="currentColor" stroke-width="2" stroke-linecap="round"><path d="M21 12a9 9 0 11-4-7.5"/><path d="M8 12l3 3 9-9"/></svg></div>
      <h3>Compliance &amp; Audit</h3>
      <p>Complete audit trails and compliance reporting to meet regulatory requirements and security standards.</p>
    </article>
    <article class="card short">
      <div class="icon-box"><svg width="22" height="22" viewBox="0 0 24 24" fill="none" stroke="currentColor" stroke-width="2" stroke-linecap="round"><path d="M5 12h14M13 6l6 6-6 6"/></svg></div>
      <h3>Cross-Application Integration</h3>
      <p>Seamless integration with existing applications and infrastructure without disrupting current workflows.</p>
    </article>
  </div>
</section>

<section class="tech">
  <span class="badge">Technical Excellence</span>
  <h2>Built for Technical Decision Makers</h2>
  <p class="lead">BrimLoop provides the robust, scalable access control infrastructure that CTOs and IT Directors need to secure their digital ecosystem.</p>
  <ul class="points">
    <li><span class="dot"><svg width="20" height="20" viewBox="0 0 24 24" fill="none" stroke="#2563eb" stroke-width="2" stroke-linecap="round"><path d="M20 12a8 8 0 11-3.5-6.6"/><path d="M8 12l3 3 8-8"/></svg></span>
      <div><h4>Policy-as-Code Architecture</h4><p>Define and version control your access policies using familiar development workflows.</p></div></li>
    <li><span class="dot"><svg width="20" height="20" viewBox="0 0 24 24" fill="none" stroke="#2563eb" stroke-width="2" stroke-linecap="round"><path d="M20 12a8 8 0 11-3.5-6.6"/><path d="M8 12l3 3 8-8"/></svg></span>
      <div><h4>High-Performance Decision Engine</h4><p>Sub-millisecond policy evaluation with horizontal scaling capabilities.</p></div></li>
    <li><span class="dot"><svg width="20" height="20" viewBox="0 0 24 24" fill="none" stroke="#2563eb" stroke-width="2" stroke-linecap="round"><path d="M20 12a8 8 0 11-3.5-6.6"/><path d="M8 12l3 3 8-8"/></svg></span>
      <div><h4>Zero-Trust Implementation</h4><p>Never trust, always verify with continuous authentication and authorization.</p></div></li>
  </ul>
  <div class="tech-visual" role="img" aria-label="Abstract dark blue background with sharp angled light beams"></div>
</section>

<section class="cta">
  <h2>Ready to Take Control of Your Digital Access?</h2>
  <p>Join leading organizations who trust BrimLoop to secure their digital infrastructure and streamline access management.</p>
  <div class="cta-actions">
    <a class="btn btn-white" href="#">Schedule Demo</a>
    <a class="btn btn-outline" href="#">Start Free Trial</a>
  </div>
</section>

<footer class="footer">
  <div class="footer-cols">
    <div>
      <a class="brand" href="#"><span class="brand-dot"></span>BrimLoop</a>
      <p class="tag">The traffic controller for digital access and data permissions.</p>
    </div>
    <div><h4>Product</h4><ul><li>Features</li><li>Pricing</li><li>Documentation</li></ul></div>
    <div><h4>Company</h4><ul><li>About</li><li>Careers</li><li>Contact</li></ul></div>
    <div><h4>Support</h4><ul><li>Help Center</li><li>Community</li><li>Status</li></ul></div>
  </div>
  <div class="footer-bottom">© 2024 BrimLoop. All rights reserved.</div>
</footer>

</body>
</html>
```